Birchwell Pantry Co - labels

I have my logo now so its time to proceed with the labels.
The product is organic juices and smoothies. They will be served in Mason jar's and sold as a premium hand made product into the CBD and outlets around Perth such as yoga studios gyms, cafe's etc. Cleanses to individuals etc.
I have attached the logo and a mock of what I would like to see.
I think the logo and the raw organic, handmade look will work with the Chalkboard design and maybe some bunting to brighten the design.
There is currently approx. 10 Juices and Smoothies to the range so I will need to settle on the design and then have you create a label for each one, once settled on the design.
If you have any questions please let me know.

Text on label:
Raw, Organic, Hand Made, Gluten-Free, Dairy-Free

Juice
Morning Tide Mix
Kale, Apple, Celery, Dandelion, Lemon & Ginger

This product is FRESH. Shake before you enjoy!!!

Label size. highest point for height 70 - 75mm. Length 200mm
I also have more wording and nutritional guide for Australian Standards. I will update soon.
Thank you

    Happy Friday Designers!!!

Well I have just increased the budget to $300. I hope this helps to get some designs coming through. If you need anything else from me please send a message.

I look forward to receiving your designs soon and thank you for working with me on my business. this is such an exciting time for me and you guys are making my dream a reality so thank you for your time.

Regards,

Denise

Reason: I have not received many designs so extending for a few more days.

• Wording - Hand Made
Raw, Organic, Gluten-Free, Dairy-Free
• A chalk board with Juice or Smoothie - Name and ingredients
Bunting I think will work well with the design of logo and chalk board plus bring some colour.

```html
<!DOCTYPE html>
<html lang="en">
<head>
<meta charset="utf-8">
<title>Birchwell Pantry Co – Morning Tide Mix label</title>
<link rel="stylesheet" href="https://fonts.googleapis.com/css2?family=Open+Sans:wght@600;700;800&family=Amatic+SC:wght@700&family=Patrick+Hand&display=swap">
<style>
  :root {
    --page: #ffffff;
    --leaf: #8cc63f;
    --leaf-pale: #e9f4d2;
    --frame: #cfe8b4;
    --ring: #cfe6b8;
    --lemon: #dde51f;
    --ink-green: #14673a;
    --bunting: #2f9e52;
    --board: #086634;
    --board-edge: #2db45e;
    --chalk: #ffffff;
    --juice: #f6a24a;
  }
  * { margin: 0; padding: 0; box-sizing: border-box; }
  html, body { width: 1200px; height: 1000px; overflow: hidden; background: var(--page); }
  .label {
    position: absolute; left: 377px; top: 181px; width: 462px; height: 677px;
    background:
      radial-gradient(ellipse 260px 300px at 266px 210px, #ffffff 0%, rgba(255,255,255,0.85) 40%, rgba(255,255,255,0) 100%),
      linear-gradient(180deg, var(--leaf-pale) 0%, var(--leaf) 70%, var(--leaf) 100%);
    overflow: hidden;
  }
  .label-art { position: absolute; inset: 0; }
  .brand-name {
    font-family: "Open Sans", sans-serif; font-weight: 800; font-size: 30px;
    fill: var(--chalk); text-anchor: middle;
  }
  .claim {
    font-family: "Open Sans", sans-serif; font-weight: 700; font-size: 22px;
    fill: var(--ink-green); text-anchor: middle; letter-spacing: 0.5px;
  }
  .chalkboard {
    position: absolute; left: 100px; top: 370px; width: 271px; height: 264px;
    background: var(--board); border: 10px solid var(--board-edge);
    color: var(--chalk);
  }
  .chalkboard span { position: absolute; white-space: nowrap; }
  .blend-name {
    left: 0; right: 0; top: 22px; text-align: center;
    font-family: "Amatic SC", sans-serif; font-weight: 700; font-size: 40px; line-height: 1;
  }
  .ingredient { font-family: "Patrick Hand", cursive; font-size: 22px; line-height: 1; }
  .product-type {
    left: 0; right: 0; top: 206px; text-align: center;
    font-family: "Patrick Hand", cursive; font-size: 34px; letter-spacing: 2px; line-height: 1;
  }
  .glass-badge { position: absolute; left: 63px; top: 350px; }
  .freshness {
    position: absolute; left: 0; right: 0; top: 648px; text-align: center;
    font-family: "Open Sans", sans-serif; font-weight: 600; font-size: 18.5px; color: var(--chalk);
  }
</style>
</head>
<body>
<div class="label">
  <svg class="label-art" width="462" height="677" viewBox="0 0 462 677">
    <defs>
      <path id="claim-arc" d="M 76 150 A 190 190 0 0 0 456 150"/>
    </defs>
    <rect class="frame-bar" x="25" y="127" width="30" height="510" fill="var(--frame)"/>
    <rect class="frame-bar" x="410" y="127" width="28" height="510" fill="var(--frame)"/>
    <circle class="logo-ring" cx="266" cy="159" r="158" fill="var(--ring)"/>
    <circle class="logo-disc" cx="266" cy="159" r="145" fill="var(--lemon)"/>
    <text class="brand-name" x="266" y="150">Birchwell</text>
    <text class="brand-name" x="266" y="186">Pantry Co</text>
    <path class="bunting" role="img" aria-label="Green bunting flags strung in an arc below the logo"
          d="M 60 154 A 206 206 0 0 0 472 154 L 444 154 A 178 178 0 0 1 88 154 Z"
          transform="translate(0 0)" fill="var(--bunting)" opacity="0.85"/>
    <text class="claim"><textPath href="#claim-arc" startOffset="16%">GLUTEN FREE</textPath></text>
    <text class="claim"><textPath href="#claim-arc" startOffset="50%">RAW ORGANIC</textPath></text>
    <text class="claim"><textPath href="#claim-arc" startOffset="85%">DAIRY FREE</textPath></text>
  </svg>

  <div class="chalkboard">
    <span class="blend-name">MORNING TIDE MIX</span>
    <span class="ingredient" style="left:3px;top:74px">Kale,</span>
    <span class="ingredient" style="left:74px;top:97px">Apple,</span>
    <span class="ingredient" style="left:159px;top:79px">Celery,</span>
    <span class="ingredient" style="left:-8px;top:152px">Dandelion,</span>
    <span class="ingredient" style="left:90px;top:136px">Lemon</span>
    <span class="ingredient" style="left:159px;top:154px">&amp; Ginger</span>
    <span class="product-type">-JUICE-</span>
  </div>

  <svg class="glass-badge" width="90" height="50" viewBox="0 0 90 50">
    <ellipse cx="45" cy="30" rx="42" ry="19" fill="var(--lemon)" stroke="var(--board-edge)" stroke-width="2"/>
    <rect role="img" aria-label="Small drawing of a juice glass with straw" x="37" y="4" width="15" height="36" rx="2" fill="var(--juice)"/>
  </svg>

  <p class="freshness">This product is fresh. Shake well before you enjoy.</p>
</div>
</body>
</html>
```